Design a menu for health restaurant

A health food restaurant in Los Angeles is seeking menu design. Our foods are made from scratch using whole ingredients.
Name: Grubb Larder
Address: 1000 E 60th StLos Angeles, CA 90247
Website: www.GrubbLarder.example
We are looking for a clean and simple menu. Brand colors are white/tan, green and orange.

Please see attached excel with menu items and logo. We do not yet have prices.

Colors
f78f20
9bcb3c
ffffff
fff3d1

Requirements
Must have
• Easy to read.
Trifold menu design (front and back).
VEGAN, VEGETARIAN, GLUTEN FREE, CONTAINS NUTS symbols.
Logo.
Nice to have
• Incorporate brand colors, but still be easy to read.
We would like to use the Belco font (attached) if it works. If not we are open to a similar font that is easy to read.

Please see attached images.
We like the images and headers of OPTION 1. Would like something similar in trifold format.
We like the clean fonts of OPTION 2.

```html
<!DOCTYPE html>
<html lang="en">
<head>
<meta charset="utf-8">
<title>Grubb Larder — Trifold Menu</title>
<link href="https://fonts.googleapis.com/css2?family=Montserrat:wght@600;700;800&family=Roboto:wght@400;500&display=swap" rel="stylesheet">
<style>
:root{
  --orange:#f26a21;
  --green:#8dc03f;
  --white:#ffffff;
  --paper:#f7f7f5;
  --ink:#222222;
  --backdrop:#e6e6e4;
}
*{box-sizing:border-box;margin:0;padding:0}
html,body{width:1200px;height:661px;overflow:hidden}
body{background:var(--backdrop);font-family:"Roboto",Arial,sans-serif;color:var(--ink);position:relative}

.sheet{position:absolute;top:106px;width:580px;height:450px;background:var(--white);display:flex;box-shadow:0 2px 8px rgba(0,0,0,.15);overflow:hidden}
.sheet--inside{left:12px}
.sheet--outside{left:608px}
.panel{width:33.333%;height:100%;display:flex;flex-direction:column;border-right:1px solid #e4e4e4;overflow:hidden}
.panel:last-child{border-right:none}

.band{font-family:"Montserrat",Arial,sans-serif;font-weight:800;color:var(--white);font-size:17px;letter-spacing:.3px;padding:0 14px;display:flex;align-items:center;height:42px;flex:none}
.band--green{background:var(--green)}
.band--orange{background:var(--orange)}

.items{padding:6px 12px 4px;display:flex;flex-direction:column;gap:6px}
.item__title{display:flex;align-items:center;gap:6px;font-family:"Montserrat",Arial,sans-serif;font-weight:700;font-size:9.5px;line-height:1.05;text-transform:uppercase}
.item__title::before{content:"";flex:none;width:16px;height:16px;border-radius:50%;border:1.2px solid currentColor}
.item--green .item__title{color:var(--green)}
.item--orange .item__title{color:var(--orange)}
.item__desc{font-size:6.2px;line-height:1.35;margin-top:3px;text-align:justify}
.item__note{display:block;font-size:4.5px;font-weight:700;color:var(--ink)}

.heading{font-family:"Montserrat",Arial,sans-serif;font-weight:800;font-size:16px;line-height:1;text-transform:uppercase;padding:10px 12px 4px}
.heading--orange{color:var(--orange)}
.heading--green{color:var(--green)}

.list{list-style:none;padding:2px 12px 0 16px}
.list li{font-size:7px;line-height:1.9}
.list li::before{content:"•";margin-right:5px}

.grid{display:grid;grid-template-columns:1fr 1fr;gap:7px 8px;padding:4px 10px}
.grid .item__title{font-size:8px}
.grid .item__desc{font-size:5.4px}

.drinks{margin-top:auto;background:var(--orange);color:var(--white);padding:8px 12px 8px;flex:none}
.drinks__title{font-family:"Montserrat",Arial,sans-serif;font-weight:800;font-size:10px;margin-bottom:4px}
.drinks__cols{display:flex;gap:14px}
.drinks__cols ul{list-style:none}
.drinks__cols li{font-size:6.4px;line-height:1.45}
.drinks__cols li::before{content:"•";margin-right:4px}
.contact{text-align:center;margin-top:8px;font-family:"Montserrat",Arial,sans-serif;font-weight:700;font-size:7.5px;line-height:1.3}
.contact__address{font-family:"Roboto",Arial,sans-serif;font-weight:400;font-size:6.5px;margin-top:4px}

.bottom-strip{margin-top:auto;height:14px;background:var(--orange);flex:none}

.cover{align-items:center;padding-top:20px}
.brand{width:104px;height:104px;border-radius:50%;border:1.5px solid var(--orange);display:flex;align-items:center;justify-content:center;gap:5px;flex-direction:column}
.brand__dot{width:14px;height:14px;border-radius:50%;background:var(--orange)}
.brand__name{font-family:"Montserrat",Arial,sans-serif;font-weight:700;font-size:11px;color:var(--orange);text-align:center;line-height:1.15}
.feature{position:relative;width:70px;height:170px;margin-top:34px;border-left:7px solid var(--green);border-right:7px solid var(--green)}
.feature__photo{position:absolute;left:50%;top:22px;transform:translateX(-50%);width:84px;height:108px;border-radius:50%;background:radial-gradient(circle at 60% 40%,#8aa64a 0%,#5d4a2e 55%,#3b2a1c 100%)}
.pill{margin-top:-14px;position:relative;background:var(--orange);color:var(--white);border-radius:14px;padding:6px 14px;text-align:center;font-size:6.8px;line-height:1.35}
</style>
</head>
<body>

<section class="sheet sheet--inside" aria-label="Inside of menu">
  <div class="panel">
    <div class="band band--green">BREAKFAST</div>
    <div class="items">
      <div class="item item--green"><div class="item__title">Pastries</div><p class="item__desc">Croissant (regular, almond, chocolate), Blueberry Muffin Superseed Cookie*</p></div>
      <div class="item item--green"><div class="item__title">Parfait</div><p class="item__desc">Fresh strawberries and blueberries on yogurt and muesli and topped with honey drizzle.</p></div>
      <div class="item item--green"><div class="item__title">Avocado Super Toast</div><p class="item__desc">Avocado Mash, Tomato, Basil, Ground Flax, Hemp Seed, Chickpeas, and Moringa Powder on Whole Wheat Bread.</p></div>
      <div class="item item--green"><div class="item__title">Brunch Burger</div><p class="item__desc">House seasoned beef burger topped with an over medium egg, red leaf lettuce, tomato, housemade pickles and Larder Sauce on a bun.</p></div>
      <div class="item item--green"><div class="item__title">Breakfast Sammy</div><p class="item__desc">Your choice of over medium egg or tofu steak with guacamole, tomato, and Larder sauce on an English muffin.</p></div>
      <div class="item item--green"><div class="item__title">AM Burrito</div><p class="item__desc">Scrambled eggs, onion, red bell pepper, black beans, housemade salsa, yogurt, and pepper jack cheese in a tortilla.</p></div>
    </div>
    <div class="band band--orange" style="margin-top:auto">SMOOTHIES</div>
    <div class="items" style="padding-bottom:10px">
      <div class="item item--orange"><div class="item__title">Green Machine Smoothie</div><p class="item__desc">Romaine, spinach, banana, mango, pineapple, flaxmilk, spirulina, almond butter</p></div>
    </div>
  </div>

  <div class="panel">
    <div class="items" style="padding-top:10px">
      <div class="item item--orange"><div class="item__title">Acai Smoothie</div><p class="item__desc">Acai, blueberries, banana, pineapple, Macqui berry, flaxmilk, almond butter</p></div>
      <div class="item item--orange"><div class="item__title">Mango Smoothie</div><p class="item__desc">Mango, flaxmilk, banan, hemp seeds</p></div>
    </div>
    <div class="band band--green" style="margin-top:6px">BOWLS</div>
    <div class="items">
      <div class="item item--green"><div class="item__title">Southwest Bowl</div><p class="item__desc">Your choice of protein with corn, black beans, red onions, almonds and avocado over quinoa with lime hot sauce.</p></div>
      <div class="item item--green"><div class="item__title">Chimi Bowl</div><p class="item__desc">Your choice of protein with red bell pepper, mushrooms, zucchini, squash, onion, cherry tomatoes and fresh herb chimichurri on wild and brown rice.</p></div>
      <div class="item item--green"><div class="item__title">Soba Noodle Bowl</div><p class="item__desc">Your choice of protein with spinach, snow peas, roasted carrots, red bell pepper, cilantro, sesame seeds and ginger lime sauce over soba noodles.</p></div>
      <div class="item item--green"><div class="item__title">Hollywood Bowl</div><p class="item__desc">Your choice of protein with broccoli, roasted corn, cherry tomatoes, basil, pepitas, flax seeds and lemon juice on wild and brown rice.</p></div>
      <div class="item item--green"><div class="item__title">Larder Bowl</div><p class="item__desc">Your choice of protein with roasted chickpeas and cauliflower, zesty fennel salad and citrus yogurt.</p></div>
      <div class="item item--green"><div class="item__title">Buddha Bowl</div><p class="item__desc">Your choice of protein with corn, red kale, sweet potatoes, red cabbage, parsley, oregano, hummus, and farro.</p></div>
    </div>
  </div>

  <div class="panel">
    <div class="items" style="padding-top:10px">
      <div class="item item--green"><div class="item__title">Chili Rice Bowl</div><p class="item__desc">Chicken, onions, bell peppers, jalapeños, black &amp; kidney beans, and tomato over brown rice.</p></div>
    </div>
    <div class="band band--orange" style="margin-top:4px">SOUPS</div>
    <div class="items">
      <div class="item item--orange"><div class="item__title">Chicken Noodle</div><p class="item__desc">Chicken, egg noodles, root vegetables, oregano &amp; peppercorns.</p></div>
      <div class="item item--orange"><div class="item__title">Larder Chili</div><p class="item__desc">Chicken, onions, bell peppers, jalapeños, black &amp; kidney beans, and tomato.</p></div>
      <div class="item item--orange"><div class="item__title"><span>Seasonal Rotating<span class="item__note">(Butternut Squash Soup V+, GF)</span></span></div><p class="item__desc">Butternut squash blended with warm spices, and coconut milk.</p></div>
    </div>
    <div class="band band--green" style="margin-top:6px">WRAPS</div>
    <div class="items">
      <div class="item item--green"><div class="item__title">Rancher's Wrap</div><p class="item__desc">Tomato, red onion, hard boiled egg, avocado, feta cheese, microgreens, romaine, grilled chicken and Ranch dressing in a grilled wrap.</p></div>
      <div class="item item--green"><div class="item__title">Vegan Tuna Wrap</div><p class="item__desc">Vegan tuna, romaine, avocado, celery, shallot, and oregano with Herbalicious Sauce in a whole grain wrap.</p></div>
      <div class="item item--green"><div class="item__title">Vegetarian Wrap</div><p class="item__desc">Roasted chickpeas, romaine, avocado, cucumber, red bell pepper, shaved carrots, cucumber, spinach, basil, black beans and feta with lemon-hummus in a sprouted 7-grain wrap.</p></div>
    </div>
    <div class="bottom-strip" style="height:4px"></div>
  </div>
</section>

<section class="sheet sheet--outside" aria-label="Outside of menu">
  <div class="panel">
    <h2 class="heading heading--orange">Salad</h2>
    <div class="items">
      <div class="item item--orange"><div class="item__title">Avocado, Golden Beet,<br>and Cranberry Salad</div><p class="item__desc">Gold beets, avocado, dried cranberries, watermelon radish, red kale, romaine, mixed greens, and pepitas served with Golden Buddha dressing.</p></div>
      <div class="item item--orange"><div class="item__title">Burrata Salad</div><p class="item__desc">Tomato, melon, shredded basil, balsamic glaze, fresh cracked pepper, and olive oil with burrata.</p></div>
      <div class="item item--orange"><div class="item__title">Mediterranean Salad</div><p class="item__desc">Cucumbers, Kalamata olives, cherry tomatoes, parsley, tricolor quinoa, hard-boiled egg, and hummus on mixed greens, romaine, and red cabbage with lemon-olive oil dressing.</p></div>
      <div class="item item--orange"><div class="item__title">Vegan Chef Salad</div><p class="item__desc">Roasted potatoes and carrots, chickpeas, avocado, microgreens and walnuts on mixed greens, romaine, and red kale with vegan ranch.</p></div>
      <div class="item item--orange"><div class="item__title">Rancher's Salad</div><p class="item__desc">Tomato, red onion, hard boiled egg, avocado, feta cheese, microgreens, and grilled chicken on romaine with Ranch dressing.</p></div>
    </div>
    <h2 class="heading heading--green" style="padding-top:8px">Burgers N'<br>Sammies</h2>
    <ul class="list">
      <li>Air Fried Chicken Sammy</li>
      <li>Grilled Chicken Sammy</li>
      <li>Classic Beef Burger</li>
      <li>Black Bean Pine Nut Burger</li>
      <li>Salmon Burger</li>
    </ul>
    <div class="bottom-strip"></div>
  </div>

  <div class="panel">
    <h2 class="heading heading--green">Snacks N'<br>Sides</h2>
    <div class="grid">
      <div class="item item--green"><div class="item__title">Fries</div><p class="item__desc">Chicken, onions, bell peppers, jalapeños, black &amp; kidney beans, and tomato over brown rice.</p></div>
      <div class="item item--green"><div class="item__title">Side<br>Salad</div><p class="item__desc">Your choice of House, Golden Beet, Mediterranean, or Vegan Chef side salad. (24oz)</p></div>
      <div class="item item--green"><div class="item__title">Guac &amp;<br>Chips</div><p class="item__desc">Guacamole with blue corn tortilla chips.</p></div>
      <div class="item item--green"><div class="item__title">Hummus &amp;<br>Chips</div><p class="item__desc">Hummus with blue corn tortilla chips.</p></div>
    </div>
    <h2 class="heading heading--orange" style="padding-top:6px">Desserts</h2>
    <div class="grid">
      <div class="item item--orange"><div class="item__title">Cookies</div><p class="item__desc">Your choice of Chocolate Chip or Double Chocolate Chip fresh baked cookie.</p></div>
      <div class="item item--orange"><div class="item__title">Fruit +<br>Spices</div><p class="item__desc">Strawberry, pineapple, green apple, orange, and blueberries with lime and chili seasoning.</p></div>
      <div class="item item--orange"><div class="item__title">Date<br>Coffee Cake</div><p class="item__desc">Signature date coffee cake with walnuts.</p></div>
      <div class="item item--orange"><div class="item__title" style="font-size:6px">Larder<br>Chocolate<br>Mousse</div><p class="item__desc">Served with grated dark chocolate.</p></div>
    </div>
    <div class="drinks">
      <div class="drinks__title">DRINKS</div>
      <div class="drinks__cols">
        <ul><li>Coffee</li><li>Power Date Shake</li><li>Heart Beet Juice</li><li>Green Leafy Juice</li><li>Orange Turmeric Juice</li></ul>
        <ul><li>Fireshot</li><li>Lemonade</li><li>Tea</li><li>Bottled Drinks</li></ul>
      </div>
      <div class="contact">(555) 014-2290<br>www.GrubbLarder.example
        <div class="contact__address">2417 W 83rd St Los Angeles, CA 90247</div>
      </div>
    </div>
  </div>

  <div class="panel cover">
    <div class="brand">
      <span class="brand__dot"></span>
      <span class="brand__name">Grubb Larder</span>
    </div>
    <div class="feature">
      <div class="feature__photo" role="img" aria-label="Photo of a plated chicken dish with sliced avocado"></div>
    </div>
    <div class="pill">(555) 014-2290<br>www.GrubbLarder.example</div>
  </div>
</section>

</body>
</html>
```